Corliss Homes Website for luxury custom home builder with endless detail

Modern website for luxury custom home builder. Simple and easy for viewers to understand what we do. New company formed by retired custom home builder. Company concept is to simplify the building experience with modern technology and introduce a simple pricing strategy for the client. Website must flow. Prefer page less design or possibly something that is up and coming within the web design community. Two galleries: INTERIOR and EXTERIOR. I would like two click on box's when the website is opened showing the galleries as a centerpiece and would also prefer them to play as a slide show. The page needs to fit the entire screen in size. We would like to use Grey, Black and White or the shade of blue that is in our company logo. I would like to see one of my uploaded photos to be in the background. I would also like a 3rd box that will play some type of animated video describing what we do and what our process is. Hoping this would be more interactive for the viewer than clicking on buttons and navigating around wasting time.

Target Market(s)

affluent buyers ages 30-60 who want to built anything from large estates to downsized luzury homes for the retired crowd.

Industry/Entity Type

Home Builder

Number of Pages Required

1 page

Font styles to use
Sans Serif

Colors
33a6d7
000000
333333
5c5c5c
9d9d9d
d9d9d9

Requirements
Must have
• Logo and name at top of page. I would like a pageless web design that includes two gallery box's (Interior and Exterior photos) side by side on the first page. I would also like a 3rd box that will be a eVideo explaining what we do and how we do it. I want as little text as possible. I would like the background to be of one of my interior photos that will flow best and pop when the page loads.

```html
<!DOCTYPE html>
<html lang="en">
<head>
<meta charset="UTF-8">
<title>Corliss Homes</title>
<link rel="stylesheet" href="https://fonts.googleapis.com/css2?family=Cinzel:wght@400;700&family=Open+Sans:wght@400;600&display=swap">
<style>
  :root {
    --blue: #33a6d7;
    --blue-dark: #2b8fbb;
    --black: #000000;
    --ink: #333333;
    --grey-dark: #5c5c5c;
    --grey: #9d9d9d;
    --grey-light: #d9d9d9;
    --white: #ffffff;
  }
  * { box-sizing: border-box; margin: 0; padding: 0; }
  html, body { width: 874px; height: 1200px; overflow: hidden; }
  body {
    position: relative;
    background: var(--white);
    font-family: "Open Sans", sans-serif;
    color: var(--ink);
  }

  /* Hero */
  .hero {
    position: absolute; left: 0; top: 0; width: 874px; height: 472px;
    background:
      linear-gradient(180deg, #3f8fd6 0%, #7fb8e6 28%, #b9c9b0 42%, #8a7a55 55%, #2f9fd0 70%, #c9c1b2 86%, #8f8572 100%);
  }
  .brand {
    position: absolute; top: 14px; left: 50%; transform: translateX(-50%);
    display: flex; flex-direction: column; align-items: center; gap: 4px;
  }
  .brand-square {
    width: 40px; height: 40px; background: var(--blue); border: 2px solid var(--white);
  }
  .brand-name {
    font-family: "Cinzel", serif; font-size: 12px; color: var(--white); letter-spacing: 0.5px;
  }
  .hero-title {
    position: absolute; top: 110px; width: 100%; text-align: center;
    font-family: "Cinzel", serif; font-weight: 700; font-size: 64px;
    color: var(--white); letter-spacing: 2px;
    text-shadow: 0 2px 6px rgba(0,0,0,0.3);
  }
  .slider-arrow {
    position: absolute; top: 228px; width: 28px; height: 36px;
    background: rgba(0,0,0,0.55); display: flex; align-items: center; justify-content: center;
  }
  .slider-arrow.prev { left: 0; }
  .slider-arrow.next { right: 0; }

  /* Gallery */
  .gallery-title {
    position: absolute; top: 512px; width: 100%; text-align: center;
    font-family: "Cinzel", serif; font-size: 38px; color: var(--ink);
  }
  .gallery-title .accent { color: var(--blue); }
  .tile {
    position: absolute; top: 575px; height: 167px;
  }
  .tile-media {
    width: 100%; height: 100%; position: relative;
    display: flex; align-items: center; justify-content: center;
  }
  .tile-interior { left: 52px; width: 245px; }
  .tile-interior .tile-media { background: linear-gradient(135deg, #6f8a8a 0%, #9fb2ac 45%, #5f6f6a 100%); }
  .tile-exterior { left: 315px; width: 238px; }
  .tile-exterior .tile-media { background: linear-gradient(160deg, #c89a78 0%, #a87658 45%, #6e8a55 80%, #8a7a66 100%); }
  .tile-video { left: 574px; width: 244px; }
  .tile-video .tile-media { background: linear-gradient(180deg, #6fb0df 0%, #b9cbd6 40%, #9a8a78 75%, #6e6356 100%); }
  .tile-label {
    position: absolute; top: 185px; left: 0; width: 100%; text-align: center;
    font-family: "Cinzel", serif; font-size: 22px; color: var(--ink);
  }
  .tile-interior .tile-label { color: var(--blue); }

  /* Welcome */
  .welcome {
    position: absolute; left: 55px; top: 824px; width: 763px; height: 210px;
    background: var(--blue); color: var(--white);
  }
  .welcome-title {
    position: absolute; top: 28px; width: 100%; text-align: center;
    font-family: "Cinzel", serif; font-size: 38px; color: var(--white);
  }
  .welcome-title .muted { color: #1f7fae; }
  .welcome-text {
    position: absolute; left: 30px; top: 100px; width: 450px;
    font-size: 11.5px; line-height: 1.55;
  }
  .welcome-brand {
    position: absolute; right: 60px; top: 96px;
    display: flex; flex-direction: column; align-items: center; gap: 8px;
  }
  .welcome-brand .brand-square { width: 64px; height: 64px; background: transparent; border: 3px solid var(--white); }
  .welcome-brand .brand-name { font-size: 14px; }

  /* Footer */
  .contact-band {
    position: absolute; left: 0; top: 1048px; width: 874px; height: 109px;
    background: #eeeeee;
  }
  .contact-item {
    position: absolute; top: 28px; display: flex; align-items: center; gap: 16px;
    font-size: 12px; color: var(--grey-dark); line-height: 1.8;
  }
  .contact-item.address { left: 170px; }
  .contact-item.phone { left: 478px; }
  .contact-icon {
    width: 48px; height: 48px; border-radius: 50%; background: var(--blue);
    display: flex; align-items: center; justify-content: center; flex-shrink: 0;
  }
  .contact-item.phone .contact-icon { background: var(--white); }
  .copyright {
    position: absolute; left: 0; top: 1157px; width: 874px; height: 43px;
    background: var(--blue); color: var(--white);
    font-size: 11px; text-align: center; line-height: 43px;
  }
</style>
</head>
<body>
  <header class="hero" role="img" aria-label="Photo of a luxury home courtyard with pool, arched patio and lounge chairs">
    <div class="brand">
      <div class="brand-square"></div>
      <div class="brand-name">Corliss Homes</div>
    </div>
    <h1 class="hero-title">CORLISS HOMES</h1>
    <div class="slider-arrow prev">
      <svg width="10" height="14" viewBox="0 0 10 14"><path d="M8 1 L2 7 L8 13" fill="none" stroke="#fff" stroke-width="2"/></svg>
    </div>
    <div class="slider-arrow next">
      <svg width="10" height="14" viewBox="0 0 10 14"><path d="M2 1 L8 7 L2 13" fill="none" stroke="#fff" stroke-width="2"/></svg>
    </div>
  </header>

  <h2 class="gallery-title"><span class="accent">Corliss Homes</span> Gallery</h2>

  <section class="tile tile-interior">
    <div class="tile-media" role="img" aria-label="Interior gallery slideshow of a home living room">
      <svg width="60" height="40" viewBox="0 0 60 40">
        <rect x="0" y="0" width="28" height="40" fill="#33a6d7"/>
        <path d="M8 14 L14 20 L8 26 M20 14 L14 20 L20 26" fill="none" stroke="#fff" stroke-width="2"/>
        <rect x="30" y="0" width="30" height="40" fill="#33a6d7"/>
        <path d="M40 12 L52 20 L40 28 Z" fill="#fff"/>
      </svg>
    </div>
    <div class="tile-label">Interior</div>
  </section>

  <section class="tile tile-exterior">
    <div class="tile-media" role="img" aria-label="Exterior gallery slideshow of a home patio with arches"></div>
    <div class="tile-label">Exterior</div>
  </section>

  <section class="tile tile-video">
    <div class="tile-media" role="img" aria-label="Video explaining the building process, over a home courtyard">
      <svg width="52" height="52" viewBox="0 0 52 52">
        <circle cx="26" cy="26" r="24" fill="rgba(255,255,255,0.85)"/>
        <path d="M21 16 L36 26 L21 36 Z" fill="#33a6d7"/>
      </svg>
    </div>
    <div class="tile-label">What we Do ?</div>
  </section>

  <section class="welcome">
    <h2 class="welcome-title"><span class="muted">Welcome to</span> The Corliss Homes</h2>
    <p class="welcome-text">Every home we build begins with a conversation about how you live. Our team pairs decades of custom building experience with modern tools and simple, clear pricing, so your estate or downsized retreat comes together without surprises. From the first sketch to the final walkthrough, we manage every detail with care.</p>
    <div class="welcome-brand">
      <div class="brand-square"></div>
      <div class="brand-name">Corliss Homes</div>
    </div>
  </section>

  <footer class="contact-band">
    <div class="contact-item address">
      <div class="contact-icon">
        <svg width="22" height="22" viewBox="0 0 22 22"><path d="M11 2 C6.5 2 4 5.5 4 9 C4 14 11 20 11 20 C11 20 18 14 18 9 C18 5.5 15.5 2 11 2 Z" fill="#fff"/><circle cx="11" cy="9" r="2.6" fill="#33a6d7"/></svg>
      </div>
      <div>256, Office area name<br>City, State, Country</div>
    </div>
    <div class="contact-item phone">
      <div class="contact-icon">
        <svg width="22" height="22" viewBox="0 0 22 22"><path d="M5 3 L8 3 L10 8 L8 9.5 C9 12 10 13 12.5 14 L14 12 L19 14 L19 17 C19 18 18 19 17 19 C10 19 3 12 3 5 C3 4 4 3 5 3 Z" fill="#33a6d7"/></svg>
      </div>
      <div>Phone No. : +1 123 456 7890<br>Email : info@corlisshomes.com</div>
    </div>
  </footer>
  <div class="copyright">© 2024 Corliss Homes. All Rights Reserved.</div>
</body>
</html>
```